Template Flyer- Corelune Pilates & Yoga

I am wanting a template 1 page flyer designed to use on the back ground of newsletter (faded background) and for our advertising posters in A4, A3, for Facebook and Instagram compatibility.

I have loaded an example from another Studio called Ferngully (file 3)- each time they have a new workshop to advertise a picture is placed in the little circle (so this is something I would want to do too where I can load a new picture each time a new workshop is running)- They have used the flyer like a water mark...I like this.

Our colour palette is what is on our logos and you can also visit our website for a feel for what we like www.corelunepilates.com.au

I need some of the designs edited a bit more and because of the time difference, there seems to be a 24hour period where we communicate with each other. May I please request another 2 days extension

Need extra days to review

Requirements
Must have
• Id like to have a picture in the back ground. My favourite back ground that has been produced so far is a background of both picture file 9 and 10 in either.
Nice to have
• 3 picture circles options to advertise the events/workshops I have each year.
• Brush stroke style circles (see picture attached)rather then smooth circles for the picture area (in a grey tone)
Should not have
• No BLACK colour writing or black circles

```html
<!DOCTYPE html>
<html lang="en">
<head>
<meta charset="utf-8">
<title>One Day Retreat – Corelune Pilates &amp; Yoga</title>
<link rel="stylesheet" href="https://fonts.googleapis.com/css2?family=Roboto+Condensed:wght@300;400;500&family=Roboto:wght@300;400&display=swap">
<style>
  :root {
    --teal: #1d93b5;
    --ink: #56595c;
    --stone: #8d9296;
    --brush: #9b9b9b;
    --paper: #f3f3f2;
    --page-bg: #ececec;
    --white: #ffffff;
  }
  * { box-sizing: border-box; margin: 0; padding: 0; }
  html, body {
    width: 768px; height: 1200px; overflow: hidden;
    background: var(--page-bg);
  }
  .flyer {
    position: absolute; left: 24px; top: 91px;
    width: 720px; height: 1018px;
    background: var(--paper);
    box-shadow: 0 4px 14px rgba(0,0,0,0.12);
    overflow: hidden;
    font-family: "Roboto Condensed", "Arial Narrow", sans-serif;
  }
  .backdrop-texture {
    position: absolute; inset: 0;
    background:
      radial-gradient(ellipse at 30% 20%, #fafafa 0%, rgba(250,250,250,0) 60%),
      radial-gradient(ellipse at 80% 60%, #e9e9e8 0%, rgba(233,233,232,0) 55%),
      var(--paper);
  }
  .backdrop-hangings {
    position: absolute; left: 0; top: 0; width: 134px; height: 640px;
    background: linear-gradient(90deg, rgba(214,196,170,0.55), rgba(200,215,215,0.35) 60%, rgba(243,243,242,0));
    -webkit-mask-image: linear-gradient(180deg, #000 70%, transparent);
    mask-image: linear-gradient(180deg, #000 70%, transparent);
  }
  .backdrop-bolster {
    position: absolute; right: 0; top: 650px; width: 160px; height: 368px;
    background: linear-gradient(270deg, rgba(196,214,200,0.7), rgba(215,225,215,0.4) 55%, rgba(243,243,242,0));
    -webkit-mask-image: linear-gradient(0deg, #000 70%, transparent);
    mask-image: linear-gradient(0deg, #000 70%, transparent);
  }
  .brand {
    position: absolute; left: 0; right: 0; top: 58px;
    text-align: center;
  }
  .brand-name {
    display: block;
    font-size: 34px; font-weight: 300; color: var(--stone);
    letter-spacing: 0.2px; line-height: 40px;
  }
  .brand-tagline {
    display: block; margin-top: 2px;
    font-family: "Roboto", sans-serif; font-size: 10px; font-weight: 300;
    color: var(--teal); letter-spacing: 2px;
  }
  .headline {
    position: absolute; left: 0; right: 0; top: 136px;
    text-align: center;
    font-size: 72px; font-weight: 500; color: var(--teal);
    letter-spacing: -0.5px; line-height: 1;
  }
  .gallery { position: absolute; left: 0; top: 0; width: 720px; height: 1018px; }
  .workshop {
    position: absolute; left: 411px; top: 676px; width: 248px;
  }
  .workshop-title {
    font-size: 27px; font-weight: 400; color: var(--teal);
    margin-bottom: 6px;
  }
  .workshop-copy {
    font-family: "Roboto", sans-serif; font-size: 10px; line-height: 12.5px;
    color: var(--ink); text-align: justify; margin-bottom: 8px;
  }
  .details { position: absolute; left: 67px; top: 730px; }
  .detail-row { display: flex; height: 36px; margin-bottom: 15px; }
  .detail-label {
    background: var(--teal); color: var(--white);
    font-size: 25px; font-weight: 400;
    display: flex; align-items: center; justify-content: center;
  }
  .detail-value {
    background: var(--white); border: 1.5px solid #c9c9c9;
    color: var(--ink); font-family: "Roboto", sans-serif; font-size: 18px;
    display: flex; align-items: center; padding-left: 14px;
  }
  .detail-value.centered { justify-content: center; padding-left: 0; }
  .contact-bar {
    position: absolute; left: 70px; top: 954px; width: 602px; height: 35px;
    background: var(--teal); border-radius: 18px;
    color: var(--white); font-family: "Roboto", sans-serif; font-size: 14px;
    display: flex; align-items: center; justify-content: center; gap: 8px;
  }
</style>
</head>
<body>
  <main class="flyer">
    <div class="backdrop-texture"></div>
    <div class="backdrop-hangings" role="img" aria-label="Faded photo of beaded hangings with coloured tassels"></div>
    <div class="backdrop-bolster" role="img" aria-label="Faded photo of a patterned yoga bolster"></div>

    <div class="brand">
      <span class="brand-name">Corelune Pilates &amp; Yoga</span>
      <span class="brand-tagline">strength in every breath</span>
    </div>

    <h1 class="headline">ONE DAY RETREAT</h1>

    <svg class="gallery" viewBox="0 0 720 1018">
      <defs>
        <clipPath id="clip-main"><circle cx="428" cy="440" r="186"/></clipPath>
        <clipPath id="clip-small-top"><circle cx="130" cy="447" r="68"/></clipPath>
        <clipPath id="clip-small-bottom"><circle cx="212" cy="574" r="98"/></clipPath>
        <linearGradient id="tone-studio" x1="0" y1="0" x2="1" y2="1">
          <stop offset="0" stop-color="#e8e6e2"/>
          <stop offset="0.45" stop-color="#c9c3b8"/>
          <stop offset="0.75" stop-color="#7d7f80"/>
          <stop offset="1" stop-color="#b9cdb0"/>
        </linearGradient>
        <linearGradient id="tone-cushions" x1="0" y1="0" x2="1" y2="1">
          <stop offset="0" stop-color="#b9c7cf"/>
          <stop offset="1" stop-color="#6f8694"/>
        </linearGradient>
        <linearGradient id="tone-tassels" x1="0" y1="0" x2="1" y2="0">
          <stop offset="0" stop-color="#c79a63"/>
          <stop offset="0.55" stop-color="#e9e4dc"/>
          <stop offset="1" stop-color="#b7c4c4"/>
        </linearGradient>
      </defs>

      <g role="img" aria-label="Workshop photo: yoga studio with mats, cork blocks and patterned bolsters">
        <rect x="230" y="240" width="400" height="400" fill="url(#tone-studio)" clip-path="url(#clip-main)"/>
      </g>
      <g fill="none" stroke="var(--brush)" stroke-linecap="round">
        <circle cx="428" cy="440" r="190" stroke-width="9" stroke-dasharray="420 18 260 30 380 14"/>
        <circle cx="426" cy="442" r="194" stroke-width="3" stroke-dasharray="180 60 240 90" opacity="0.7"/>
      </g>

      <g role="img" aria-label="Workshop photo: pile of patterned cushions">
        <rect x="60" y="377" width="140" height="140" fill="url(#tone-cushions)" clip-path="url(#clip-small-top)"/>
      </g>
      <g fill="none" stroke="var(--brush)" stroke-linecap="round">
        <circle cx="130" cy="447" r="71" stroke-width="6" stroke-dasharray="150 10 200 8"/>
      </g>

      <g role="img" aria-label="Workshop photo: coloured tassels hanging by a doorway">
        <rect x="112" y="474" width="200" height="200" fill="url(#tone-tassels)" clip-path="url(#clip-small-bottom)"/>
      </g>
      <g fill="none" stroke="var(--brush)" stroke-linecap="round">
        <circle cx="212" cy="574" r="102" stroke-width="8" stroke-dasharray="260 12 280 16 60"/>
        <circle cx="210" cy="576" r="105" stroke-width="2" stroke-dasharray="120 80 200 60" opacity="0.7"/>
      </g>
    </svg>

    <section class="workshop">
      <h2 class="workshop-title">OUR WORKSHOP</h2>
      <p class="workshop-copy">Lorem Ipsum is simply dummy text of the printing and typesetting industry. Lorem Ipsum has been the industry's standard dummy text ever since the 1500s, when an unknown printer took a galley of type and scrambled it to make a type specimen book.</p>
      <p class="workshop-copy">Lorem Ipsum is simply dummy text of the printing and typesetting industry. Lorem Ipsum has been the industry's standard dummy text ever since the 1500s, when an unknown printer took a galley of type and scrambled it to make a type specimen book.</p>
    </section>

    <section class="details">
      <div class="detail-row">
        <div class="detail-label" style="width:69px">DATE</div>
        <div class="detail-value" style="width:236px">SUNDAY, XX-XX-2018</div>
      </div>
      <div class="detail-row">
        <div class="detail-label" style="width:69px">TIME</div>
        <div class="detail-value" style="width:201px">XX am to XX pm</div>
      </div>
      <div class="detail-row">
        <div class="detail-label" style="width:121px">COST</div>
        <div class="detail-value centered" style="width:145px">$XX</div>
      </div>
      <div class="detail-row">
        <div class="detail-label" style="width:121px">LOCATION</div>
        <div class="detail-value" style="width:396px">LOREM IPSUM IS SIMPLY DUMMY TEXT</div>
      </div>
    </section>

    <footer class="contact-bar">
      <span>(03)5550 1284</span><span>|</span>
      <span>www.corelunepilatesandyoga.com</span><span>|</span>
      <span>info@corelunepilatesandyoga.com</span>
    </footer>
  </main>
</body>
</html>
```